Travel Company is looking for a STAND OUT Business Card

I need a unique Business Card that will truly stand out. Nothing too busy. Simple is good, right? Not looking for a standard design either. No cookie cutter layout. We are a Travel Company that works more with Companies than Travelers. I had an idea to focus and emphasis on the 2 logo a bit more. This is not necessary, however thought it would look interesting. I am just looking for something interesting and a bit different. Does't have to completely off the wall crazy, just not your run of the mill business card.

Target Market(s)

Hoteliers, Resort Management, Call Centers, Executives, Travelers, Families, Businesses

Industry/Entity Type

Hospitality

Contact Information for Business Card

President/CEO - Marcus T Bellamy (title not necessary if design doesn't allow for it)
contact - (407) 555-0186
email - mbellamy@wayfarenow.example
address - 4812 Quillmore Ave #164
Orlando, FL 32804
website - www.wayfarenow.example

Font styles to use
Serif
Other font styles liked:
• Avenir Next LT Pro BOLD

Requirements
Must have
• simple look and design. Unique design
Nice to have
• I attached the 2 logo separate from the main logo. This can be used separately from the Main Logo, together with the main logo or as main logo. I included the logo font. Use it or not, designers choice.
Should not have
• cookie cutter design. Little use of red other than the logo

```html
<!DOCTYPE html>
<html lang="en">
<head>
<meta charset="utf-8">
<title>Wayfare Now – Business Card</title>
<link rel="stylesheet" href="https://fonts.googleapis.com/css2?family=Libre+Baskerville:wght@400;700&family=Questrial&display=swap">
<style>
  :root {
    --backdrop: #2b2b2b;
    --card-light: #ffffff;
    --card-dark: #231f20;
    --map-pink: #f2666e;
    --map-pink-soft: #f6a0a5;
    --map-grey: #9a9a9a;
    --map-grey-deep: #7d7d7d;
    --brand-red: #ee1c24;
    --ink: #111111;
    --text-light: #f2f2f2;
    --text-muted: #c9c9c9;
  }
  * { margin: 0; padding: 0; box-sizing: border-box; }
  html, body { width: 1200px; height: 1000px; overflow: hidden; background: var(--backdrop); }
  .canvas { position: relative; width: 1200px; height: 1000px; }

  .card { position: absolute; width: 712px; height: 434px; overflow: hidden; }
  .card--front { left: 32px; top: 30px; background: var(--card-light); }
  .card--back { left: 415px; top: 512px; background: var(--card-dark); }

  .map-area { position: absolute; display: block; }
  .card--front .map-area { inset: 0; width: 712px; height: 434px; }
  .card--back .map-area { left: 0; top: 0; width: 712px; height: 434px; }

  .brand-lockup {
    position: absolute; display: flex; align-items: center; gap: 14px;
    font-family: "Libre Baskerville", Georgia, serif; font-weight: 700; color: var(--ink);
  }
  .brand-lockup__dot { border-radius: 50%; background: var(--brand-red); flex: none; }
  .card--front .brand-lockup { left: 72px; top: 170px; font-size: 72px; letter-spacing: -1px; }
  .card--front .brand-lockup__dot { width: 46px; height: 46px; }
  .card--back .brand-lockup { left: 20px; top: 178px; font-size: 22px; gap: 6px; }
  .card--back .brand-lockup__dot { width: 14px; height: 14px; }

  .contact {
    position: absolute; right: 44px; top: 80px; text-align: right;
    font-family: "Libre Baskerville", Georgia, serif; color: var(--text-light);
  }
  .contact__name { font-size: 20px; letter-spacing: 0.5px; line-height: 1; }
  .contact__title { font-family: "Questrial", Arial, sans-serif; font-size: 17px; color: var(--text-muted); margin-top: 21px; }
  .contact__line { font-size: 19px; margin-top: 27px; line-height: 1; }
  .contact__line:first-of-type { margin-top: 31px; }
  .contact__label { color: var(--brand-red); font-weight: 700; margin-right: 6px; }
</style>
</head>
<body>
<main class="canvas">

  <section class="card card--front">
    <svg class="map-area" role="img" aria-label="Map of Europe, Africa and Asia in pink with a dashed travel route" viewBox="0 0 712 434">
      <defs>
        <linearGradient id="front-map-tone" x1="0" y1="0" x2="1" y2="1">
          <stop offset="0" stop-color="var(--map-pink)"/>
          <stop offset="0.55" stop-color="var(--map-pink)"/>
          <stop offset="1" stop-color="var(--map-pink-soft)"/>
        </linearGradient>
      </defs>
      <rect width="712" height="434" fill="url(#front-map-tone)"/>
      <path d="M0 350 C 120 320, 200 380, 330 320 S 560 180, 712 110" fill="none" stroke="#222" stroke-width="2" stroke-dasharray="8 6"/>
    </svg>
    <div class="brand-lockup">
      <span class="brand-lockup__dot"></span>
      <span class="brand-lockup__name">wayfarenow</span>
    </div>
  </section>

  <section class="card card--back">
    <svg class="map-area" role="img" aria-label="Grey map of North America and the North Atlantic with a dashed flight path" viewBox="0 0 712 434">
      <defs>
        <linearGradient id="back-map-tone" x1="0" y1="0" x2="1" y2="0">
          <stop offset="0" stop-color="var(--map-grey)"/>
          <stop offset="0.45" stop-color="var(--map-grey-deep)"/>
          <stop offset="0.6" stop-color="var(--card-dark)"/>
        </linearGradient>
      </defs>
      <rect width="712" height="434" fill="url(#back-map-tone)"/>
      <path d="M0 410 C 80 400, 150 395, 230 410 C 300 370, 420 370, 560 390" fill="none" stroke="var(--brand-red)" stroke-width="1.6" stroke-dasharray="7 5"/>
    </svg>
    <div class="brand-lockup">
      <span class="brand-lockup__dot"></span>
      <span class="brand-lockup__name">wayfarenow</span>
    </div>
    <div class="contact">
      <p class="contact__name">RHYS CALLOWAY</p>
      <p class="contact__title">Travel Expert</p>
      <p class="contact__line"><span class="contact__label">w.</span>www.wayfarenow.example</p>
      <p class="contact__line"><span class="contact__label">e.</span>rcalloway@wayfarenow.example</p>
      <p class="contact__line"><span class="contact__label">m.</span>0491570156</p>
    </div>
  </section>

</main>
</body>
</html>
```